"Fold The Map" A Song about getting better!

For my next Single i would like a cover around the concept "Fold the Map" meaning getting better than how you are now :)
I have attached the Picture and an idea for the title font. Mainly its the font that i would like you to design. It only has to be shaped like a stair but should be much more in shape and Color and has to fit in the Picture smoothly. There's also my artist logo which has to be attached to the cover :)
you are free to use colors, effects, filters or whatever your awesome creativity comes up with :P thanks! this is a great site!

Font styles to use
Decorative

Requirements
Must have
• designed and creative title font.

```html
<!DOCTYPE html>
<html lang="en">
<head>
<meta charset="utf-8">
<title>Fold The Map – Single Cover</title>
<link href="https://fonts.googleapis.com/css2?family=Monoton&display=swap" rel="stylesheet">
<style>
  :root {
    --paper: #ffffff;
    --sun: #ffef00;
    --sun-deep: #f7c800;
    --stone-light: #c9bd9a;
    --stone-mid: #9a927f;
    --stone-dark: #6e6a60;
    --boot-teal: #3c5a66;
    --boot-violet: #7a3f9a;
    --title: #ffffff;
    --title-line: #2a2a2a;
    --artist: #111111;
  }
  * { margin: 0; padding: 0; box-sizing: border-box; }
  html, body { width: 1200px; height: 1000px; overflow: hidden; background: var(--paper); }
  .cover {
    position: relative;
    width: 1200px;
    height: 1000px;
    background: var(--paper);
    overflow: hidden;
  }
  .cover__backdrop {
    position: absolute;
    inset: 0;
  }
  .title {
    position: absolute;
    font-family: "Monoton", sans-serif;
    color: var(--title);
    text-shadow: 2px 2px 0 var(--title-line), -1px -1px 0 rgba(0,0,0,0.25);
    line-height: 1;
    letter-spacing: 2px;
  }
  .title__step { position: absolute; white-space: nowrap; font-size: 118px; }
  .title__step--one   { left: 300px; top: 265px; }
  .title__step--two   { left: 500px; top: 445px; }
  .title__step--three { left: 590px; top: 630px; }
  .artist-name {
    position: absolute;
    left: 820px;
    top: 760px;
    font-family: "Monoton", sans-serif;
    color: var(--artist);
    font-size: 54px;
    line-height: 1.15;
  }
  .artist-name span { display: block; }
  .artist-name span + span { padding-left: 20px; font-size: 46px; }
</style>
</head>
<body>
  <main class="cover">
    <svg class="cover__backdrop" width="1200" height="1000" viewBox="0 0 1200 1000" xmlns="http://www.w3.org/2000/svg">
      <defs>
        <radialGradient id="sun-glow" cx="50%" cy="50%" r="50%">
          <stop offset="0" stop-color="var(--sun-deep)"/>
          <stop offset="0.75" stop-color="var(--sun)"/>
          <stop offset="1" stop-color="var(--paper)" stop-opacity="0"/>
        </radialGradient>
        <linearGradient id="scene-tones" x1="0" y1="0" x2="1" y2="1">
          <stop offset="0" stop-color="var(--stone-light)"/>
          <stop offset="0.35" stop-color="var(--boot-teal)"/>
          <stop offset="0.6" stop-color="var(--boot-violet)"/>
          <stop offset="0.8" stop-color="var(--stone-mid)"/>
          <stop offset="1" stop-color="var(--stone-dark)"/>
        </linearGradient>
        <filter id="soft-edge" x="-10%" y="-10%" width="120%" height="120%">
          <feGaussianBlur stdDeviation="6"/>
        </filter>
      </defs>
      <ellipse class="sun-halo" cx="640" cy="500" rx="580" ry="520" fill="url(#sun-glow)"/>
      <ellipse class="photo-frame" cx="600" cy="475" rx="440" ry="420"
               fill="url(#scene-tones)" filter="url(#soft-edge)"
               role="img" aria-label="Photo of a worn purple and teal child's boot with loose lilac laces resting on a granite step in warm sunlight"/>
    </svg>

    <h1 class="title" aria-label="Fold The Map">
      <span class="title__step title__step--one">FOLD</span>
      <span class="title__step title__step--two">THE</span>
      <span class="title__step title__step--three">MAP</span>
    </h1>

    <p class="artist-name"><span>Milo</span><span>Rennick</span></p>
  </main>
</body>
</html>
```